Business Card design + business logo for email

My company is called Harbourline Drinks. I will be selling a range of beverages from wine, spirits, craft beer to cider. I would like the feel to be like I care about my customers business. My strength is tailoring/offering products that I know will suit their outlet & area demographic. I value strong, genuine relationships with my customers I service. Please ring me on 0417263958 for any further info you may need to get the right result.

Industry/Entity Type

Business

```html
<!DOCTYPE html>
<html lang="en">
<head>
<meta charset="utf-8">
<title>Harbourline Drinks — Business Card</title>
<link rel="stylesheet" href="https://fonts.googleapis.com/css2?family=Allura&family=EB+Garamond:ital,wght@0,500;1,600&display=swap">
<style>
  :root {
    --page-bg: #ffffff;
    --card-bg: #000000;
    --brand-gold: #f3a51c;
    --text-white: #ffffff;
  }
  * { margin: 0; padding: 0; box-sizing: border-box; }
  html, body {
    width: 1200px;
    height: 800px;
    overflow: hidden;
    background: var(--page-bg);
  }
  .canvas {
    position: relative;
    width: 1200px;
    height: 800px;
  }
  .business-card {
    position: absolute;
    left: 200px;
    top: 172px;
    width: 800px;
    height: 456px;
    background: var(--card-bg);
    color: var(--text-white);
    text-align: center;
  }
  .brand-mark {
    position: absolute;
    left: 50%;
    top: 58px;
    width: 72px;
    height: 72px;
    margin-left: -36px;
    border: 3px solid var(--brand-gold);
    border-radius: 50%;
  }
  .brand-name {
    position: absolute;
    left: 0;
    right: 0;
    top: 168px;
    font-family: "EB Garamond", Georgia, serif;
    font-weight: 500;
    font-size: 50px;
    letter-spacing: 1px;
    color: var(--brand-gold);
  }
  .contact-name {
    position: absolute;
    left: 0;
    right: 0;
    top: 288px;
    font-family: "Allura", cursive;
    font-size: 56px;
    line-height: 1;
  }
  .contact-line {
    position: absolute;
    left: 0;
    right: 0;
    font-family: "EB Garamond", Georgia, serif;
    font-style: italic;
    font-weight: 600;
    font-size: 25px;
    letter-spacing: 1.5px;
    line-height: 1;
  }
  .contact-phone { top: 360px; }
  .contact-email { top: 400px; }
</style>
</head>
<body>
  <main class="canvas">
    <section class="business-card">
      <div class="brand-mark" aria-hidden="true"></div>
      <h1 class="brand-name">Harbourline Drinks</h1>
      <p class="contact-name">Liam Farrow</p>
      <p class="contact-line contact-phone">0417263958</p>
      <p class="contact-line contact-email">liam.farrow@harbourmail.com</p>
    </section>
  </main>
</body>
</html>
```